Company providing Business Management Services needs modern business card

The business provides services like tender preparation, bank submissions, business health checks, financial and admin support. We want to portray 'Trust', 'Strength' and 'Support'.
2 styles of logo in various formats have been uploaded.
Looking for easy to understand, yet sophisticated and stand out from the crowd.

Target Market(s)

Small and Medium sized businesses

Industry/Entity Type

Business

Contact Information for Business Card

Name - Daniel Vesterby, Description - Manager, Phone - 0472 915 603, Email - danielvesterby@kpwholdingsgroup.example, Work description - Business Management Services.

Requirements
Must have
• Logo

```html
<!DOCTYPE html>
<html lang="en">
<head>
<meta charset="utf-8">
<title>KPW Holdings Group – Business Card</title>
<link rel="stylesheet" href="https://fonts.googleapis.com/css2?family=Quicksand:wght@500;600&family=Ubuntu:wght@500;700&display=swap">
<style>
  :root {
    --page-bg: #3a3d3f;
    --card-light: #f4f4f5;
    --card-mid: #d9d9db;
    --ink-dark: #3c3c3e;
    --ink-mid: #555558;
    --purple: #a05cc4;
    --blue: #4f86c8;
    --green: #6cbf4a;
    --orange: #f08a24;
  }
  * { margin: 0; padding: 0; box-sizing: border-box; }
  html, body {
    width: 1200px;
    height: 804px;
    overflow: hidden;
    background: var(--page-bg);
  }
  .canvas {
    width: 1200px;
    height: 804px;
    display: flex;
    align-items: center;
    justify-content: center;
  }
  .business-card {
    position: relative;
    width: 840px;
    height: 480px;
    background: radial-gradient(ellipse at 45% 40%, var(--card-light) 0%, #e9e9ea 55%, var(--card-mid) 100%);
    border-radius: 4px;
    box-shadow: 0 18px 40px rgba(0,0,0,0.35);
    font-family: "Quicksand", sans-serif;
    color: var(--ink-dark);
  }
  .brand {
    position: absolute;
    top: 62px;
    left: 340px;
    display: flex;
    align-items: center;
    gap: 16px;
  }
  .brand-square {
    width: 54px;
    height: 54px;
    background: var(--ink-mid);
  }
  .brand-name {
    font-family: "Quicksand", sans-serif;
    font-weight: 600;
    font-size: 34px;
    color: var(--ink-mid);
    letter-spacing: 0.5px;
  }
  .person {
    position: absolute;
    top: 182px;
    left: 0;
    width: 100%;
    text-align: center;
    padding-left: 120px;
  }
  .person-name {
    font-family: "Ubuntu", sans-serif;
    font-weight: 700;
    font-size: 54px;
    color: var(--ink-dark);
    line-height: 1;
  }
  .person-role {
    margin-top: 6px;
    font-family: "Ubuntu", sans-serif;
    font-weight: 500;
    font-size: 24px;
    letter-spacing: 1px;
    color: var(--ink-mid);
  }
  .contact {
    position: absolute;
    top: 300px;
    left: 270px;
    font-size: 20px;
    font-weight: 500;
    color: var(--ink-mid);
  }
  .contact-line {
    display: flex;
    align-items: center;
    gap: 12px;
    height: 34px;
  }
  .contact-line.phone { padding-left: 90px; font-size: 24px; }
  .contact-icon { width: 22px; height: 22px; fill: var(--ink-dark); }
  .services {
    position: absolute;
    left: 34px;
    bottom: 52px;
    font-size: 28px;
    font-weight: 500;
  }
  .values {
    position: absolute;
    right: 30px;
    bottom: 36px;
    font-size: 26px;
    font-weight: 500;
  }
  .tone-purple { color: var(--purple); }
  .tone-blue { color: var(--blue); }
  .tone-green { color: var(--green); }
  .divider { color: var(--orange); margin: 0 4px; }
</style>
</head>
<body>
<main class="canvas">
  <article class="business-card">
    <header class="brand">
      <span class="brand-square" aria-hidden="true"></span>
      <span class="brand-name">KPW Holdings Group</span>
    </header>

    <section class="person">
      <h1 class="person-name">Daniel Vesterby</h1>
      <p class="person-role">MANAGER</p>
    </section>

    <section class="contact">
      <div class="contact-line phone">
        <svg class="contact-icon" viewBox="0 0 24 24" aria-hidden="true">
          <path d="M6.6 10.8a15.1 15.1 0 0 0 6.6 6.6l2.2-2.2a1 1 0 0 1 1-.25 11.4 11.4 0 0 0 3.6.57 1 1 0 0 1 1 1V20a1 1 0 0 1-1 1A17 17 0 0 1 3 4a1 1 0 0 1 1-1h3.5a1 1 0 0 1 1 1c0 1.25.2 2.45.57 3.57a1 1 0 0 1-.25 1z"/>
        </svg>
        <span>0472 915 603</span>
      </div>
      <div class="contact-line email">
        <svg class="contact-icon" viewBox="0 0 24 24" aria-hidden="true">
          <path d="M2 5h20v14H2z M3.5 6.5 12 13l8.5-6.5" fill="none" stroke="#3c3c3e" stroke-width="1.8"/>
        </svg>
        <span>danielvesterby@kpwholdingsgroup.example</span>
      </div>
    </section>

    <p class="services">
      <span class="tone-purple">Business</span>
      <span class="tone-blue">Management</span>
      <span class="tone-green">Services</span>
    </p>

    <p class="values">
      <span class="tone-purple">Trust</span><span class="divider">|</span><span class="tone-blue">Strength</span><span class="divider">|</span><span class="tone-green">Support</span>
    </p>
  </article>
</main>
</body>
</html>
```